Feedback App to request feedback from colleagues

It’s a small web app to collect feedback from team members. This is the general screen flow but happy for variations to it.

Users logs into application and is able to see the feedback received till date from different colleagues.

At the top right are “Request feedback”, “Respond to Feedback”.

When the user clicks on Request Feedback, there are three options.
Adhoc Feedback
Mid Year Feedback
360 Feedback

Adhoc feedback will open a screen where I can search for colleagues to request feedback from (I can select more than one). There are three pre-defined question that can I edit if needed.

Mid year feedback: same process but questions cannot be edited

360 Feedback - just redirect to another website.

Respond to Feedback - see incoming request and the ability to provide feedback to questions received.

Send Feedback: select a colleague and send adhoc feedback.

Colours to be used are white and red only. Simple design, the app will be embedded in a portal so need for headers etc. think of a mobile view but no need for logo, header bar etc

Colour Codes:
Red: #E60000
White #FFFFFF
Grey: #333333 (Only use if needed e.g. borders, background etc)
Black: #000000

Only the above colours to be used

Number of Pages Required

1 page

Font styles to use
Sans Serif

Colors
EB3D1F
EC4F4E
F09395
F8D3D4
FCEDEE

Requirements
Must have
• Design screens for every page mentioned
Nice to have
• Clean design, use of images and icons
Should not have
• Cluttered design, header

```html
<!DOCTYPE html>
<html lang="en">
<head>
<meta charset="utf-8">
<title>Feedback App</title>
<link href="https://fonts.googleapis.com/css2?family=Roboto+Condensed:wght@400;700&family=Roboto:ital,wght@0,400;0,700;1,400&family=Fira+Sans:wght@500&display=swap" rel="stylesheet">
<style>
:root{
  --red:#E60000;
  --red-main:#EB3D1F;
  --red-soft:#EC4F4E;
  --pink-mid:#F09395;
  --pink-light:#F8D3D4;
  --pink-pale:#FCEDEE;
  --white:#FFFFFF;
  --grey:#333333;
  --black:#000000;
  --stage:#a79f9f;
}
*{box-sizing:border-box;margin:0;padding:0}
html,body{width:1200px;height:2266px;overflow:hidden}
body{background:radial-gradient(ellipse at center,#8f8787 0%,var(--stage) 70%,#b0a9a9 100%);font-family:'Roboto',sans-serif;position:relative}
.screen{position:absolute;left:99px;width:1002px;height:498px;overflow:hidden;
  background:linear-gradient(100deg,#f3b9bd 0%,#f8d3d4 55%,#fce6e8 100%);
  box-shadow:0 8px 30px rgba(0,0,0,.45)}
.btn{position:absolute;height:47px;width:266px;display:flex;align-items:center;justify-content:center;
  font-family:'Roboto Condensed',sans-serif;font-size:18px;font-weight:400;text-transform:uppercase;letter-spacing:.1px}
.btn-request{background:linear-gradient(180deg,#f0502f 0%,#d91c04 100%);color:var(--white);box-shadow:0 2px 4px rgba(150,0,0,.3)}
.btn-respond{background:linear-gradient(180deg,#fde9ea,#f9d6d7);border:2px solid var(--pink-mid);color:var(--red-main)}
.grid{position:absolute;left:33px;top:77px;display:grid;grid-template-columns:repeat(3,307px);grid-auto-rows:126px;gap:8px 7px}
.card{background:var(--white);position:relative}
.avatar{position:absolute;left:13px;top:22px;width:53px;height:53px}
.quote{position:absolute;left:80px;top:20px;width:198px;font-style:italic;font-size:9.6px;line-height:16px;color:#8a8a8a;text-align:justify;text-align-last:justify}
.quote span{display:block}
.quote span:last-child{text-align-last:left}
.sig{position:absolute;left:80px;top:93px;display:flex;align-items:center;gap:8px;font-family:'Roboto',sans-serif;font-weight:700;font-size:9.6px;color:var(--black)}
.stars{color:var(--red-main);font-size:11px;letter-spacing:1.5px}
.veil{position:absolute;inset:0;background:linear-gradient(100deg,rgba(236,92,78,.86) 0%,rgba(239,130,125,.82) 60%,rgba(240,147,149,.8) 100%)}
.modal{position:absolute;left:242px;top:14px;width:449px;height:290px;background:var(--white);border:2px solid var(--red-main);overflow:hidden;box-shadow:0 4px 14px rgba(120,0,0,.25)}
.modal-head{height:76px;background:var(--red-main);color:var(--white);font-family:'Roboto Condensed',sans-serif;font-weight:700;font-size:30px;display:flex;align-items:center;padding-left:82px}
.modal-close{position:absolute;left:401px;top:16px;width:48px;height:48px;border-radius:50%;background:var(--white);display:flex;align-items:center;justify-content:center}
.modal-list{list-style:none;position:absolute;left:92px;top:108px}
.modal-list li{font-family:'Fira Sans',sans-serif;font-weight:500;font-size:27px;color:var(--grey);height:53px;display:flex;align-items:center;gap:24px}
.modal-list li::before{content:"";width:13px;height:13px;border-radius:50%;background:var(--red-main)}
.page-title{position:absolute;left:33px;top:12px;font-family:'Roboto Condensed',sans-serif;font-weight:700;font-size:29px;color:var(--black)}
.search{position:absolute;left:31px;top:58px;width:384px;height:46px;background:var(--white);border:2px solid var(--pink-mid);display:flex;align-items:center;justify-content:space-between;padding:0 20px;font-size:12px;color:#777}
.questions{position:absolute;left:33px;top:119px;width:937px;height:366px;border:2px solid #e7b4b6;background:var(--white)}
.question{position:relative;height:121px;border-bottom:2px solid #eab8ba;background:#fdfafa}
.question:last-child{border-bottom:none}
.question.active{background:#f6cfd1}
.q-title{position:absolute;left:38px;top:30px;font-family:'Roboto',sans-serif;font-weight:700;font-size:14.5px;color:var(--black);letter-spacing:.1px}
.question.active .q-title{left:26px;top:15px;width:884px;height:34px;background:var(--red-main);color:var(--white);border-radius:3px;padding:0 27px;display:flex;align-items:center;justify-content:space-between}
.q-body{position:absolute;left:38px;top:62px;width:800px;font-size:11px;line-height:18px;color:var(--grey)}
.question.active .q-body{top:58px}
.q-tag{position:absolute;right:0;bottom:0;width:76px;height:23px;background:var(--red-main);color:var(--white);font-family:'Roboto Condensed',sans-serif;font-weight:700;font-size:11.5px;display:flex;align-items:center;justify-content:center}
</style>
</head>
<body>

<!-- Screen 1: received feedback -->
<section class="screen" style="top:100px">
  <div class="btn btn-request" style="left:423px;top:13px">Request Feedback</div>
  <div class="btn btn-respond" style="left:701px;top:13px">Respond to Feedback</div>
  <div class="grid">
    <div class="card"><svg class="avatar" viewBox="0 0 53 53"><circle cx="26.5" cy="26.5" r="24.5" fill="none" stroke="#f4c3c5" stroke-width="3"/><circle cx="26.5" cy="21" r="7" fill="#f4c3c5"/><path d="M13 37c0-6 6-8 13.5-8s13.5 2 13.5 8v2H13z" fill="#f4c3c5"/></svg><p class="quote"><span>“At vero eos et accusamus et io dignissimos</span><span>ducimus qui bl vero eos et accusamus et</span><span>iustodio dignissimoss qui blanditiipraesnt</span><span>iuatum deleniti atq”</span></p><div class="sig">JOHN DOE <span class="stars">★★★★★</span></div></div>
    <div class="card"><svg class="avatar" viewBox="0 0 53 53"><circle cx="26.5" cy="26.5" r="24.5" fill="none" stroke="#f4c3c5" stroke-width="3"/><circle cx="26.5" cy="21" r="7" fill="#f4c3c5"/><path d="M13 37c0-6 6-8 13.5-8s13.5 2 13.5 8v2H13z" fill="#f4c3c5"/></svg><p class="quote"><span>“At vero eos et accusamus et io dignissimos</span><span>ducimus qui bl vero eos et accusamus et</span><span>iustodio dignissimoss qui blanditiipraesnt</span><span>iuatum deleniti atq”</span></p><div class="sig">JOHN DOE <span class="stars">★★★★★</span></div></div>
    <div class="card"><svg class="avatar" viewBox="0 0 53 53"><circle cx="26.5" cy="26.5" r="24.5" fill="none" stroke="#f4c3c5" stroke-width="3"/><circle cx="26.5" cy="21" r="7" fill="#f4c3c5"/><path d="M13 37c0-6 6-8 13.5-8s13.5 2 13.5 8v2H13z" fill="#f4c3c5"/></svg><p class="quote"><span>“At vero eos et accusamus et io dignissimos</span><span>ducimus qui bl vero eos et accusamus et</span><span>iustodio dignissimoss qui blanditiipraesnt</span><span>iuatum deleniti atq”</span></p><div class="sig">JOHN DOE <span class="stars">★★★★★</span></div></div>
    <div class="card"><svg class="avatar" viewBox="0 0 53 53"><circle cx="26.5" cy="26.5" r="24.5" fill="none" stroke="#f4c3c5" stroke-width="3"/><circle cx="26.5" cy="21" r="7" fill="#f4c3c5"/><path d="M13 37c0-6 6-8 13.5-8s13.5 2 13.5 8v2H13z" fill="#f4c3c5"/></svg><p class="quote"><span>“At vero eos et accusamus et io dignissimos</span><span>ducimus qui bl vero eos et accusamus et</span><span>iustodio dignissimoss qui blanditiipraesnt</span><span>iuatum deleniti atq”</span></p><div class="sig">JOHN DOE <span class="stars">★★★★★</span></div></div>
    <div class="card"><svg class="avatar" viewBox="0 0 53 53"><circle cx="26.5" cy="26.5" r="24.5" fill="none" stroke="#f4c3c5" stroke-width="3"/><circle cx="26.5" cy="21" r="7" fill="#f4c3c5"/><path d="M13 37c0-6 6-8 13.5-8s13.5 2 13.5 8v2H13z" fill="#f4c3c5"/></svg><p class="quote"><span>“At vero eos et accusamus et io dignissimos</span><span>ducimus qui bl vero eos et accusamus et</span><span>iustodio dignissimoss qui blanditiipraesnt</span><span>iuatum deleniti atq”</span></p><div class="sig">JOHN DOE <span class="stars">★★★★★</span></div></div>
    <div class="card"><svg class="avatar" viewBox="0 0 53 53"><circle cx="26.5" cy="26.5" r="24.5" fill="none" stroke="#f4c3c5" stroke-width="3"/><circle cx="26.5" cy="21" r="7" fill="#f4c3c5"/><path d="M13 37c0-6 6-8 13.5-8s13.5 2 13.5 8v2H13z" fill="#f4c3c5"/></svg><p class="quote"><span>“At vero eos et accusamus et io dignissimos</span><span>ducimus qui bl vero eos et accusamus et</span><span>iustodio dignissimoss qui blanditiipraesnt</span><span>iuatum deleniti atq”</span></p><div class="sig">JOHN DOE <span class="stars">★★★★★</span></div></div>
    <div class="card"><svg class="avatar" viewBox="0 0 53 53"><circle cx="26.5" cy="26.5" r="24.5" fill="none" stroke="#f4c3c5" stroke-width="3"/><circle cx="26.5" cy="21" r="7" fill="#f4c3c5"/><path d="M13 37c0-6 6-8 13.5-8s13.5 2 13.5 8v2H13z" fill="#f4c3c5"/></svg><p class="quote"><span>“At vero eos et accusamus et io dignissimos</span><span>ducimus qui bl vero eos et accusamus et</span><span>iustodio dignissimoss qui blanditiipraesnt</span><span>iuatum deleniti atq”</span></p><div class="sig">JOHN DOE <span class="stars">★★★★★</span></div></div>
    <div class="card"><svg class="avatar" viewBox="0 0 53 53"><circle cx="26.5" cy="26.5" r="24.5" fill="none" stroke="#f4c3c5" stroke-width="3"/><circle cx="26.5" cy="21" r="7" fill="#f4c3c5"/><path d="M13 37c0-6 6-8 13.5-8s13.5 2 13.5 8v2H13z" fill="#f4c3c5"/></svg><p class="quote"><span>“At vero eos et accusamus et io dignissimos</span><span>ducimus qui bl vero eos et accusamus et</span><span>iustodio dignissimoss qui blanditiipraesnt</span><span>iuatum deleniti atq”</span></p><div class="sig">JOHN DOE <span class="stars">★★★★★</span></div></div>
    <div class="card"><svg class="avatar" viewBox="0 0 53 53"><circle cx="26.5" cy="26.5" r="24.5" fill="none" stroke="#f4c3c5" stroke-width="3"/><circle cx="26.5" cy="21" r="7" fill="#f4c3c5"/><path d="M13 37c0-6 6-8 13.5-8s13.5 2 13.5 8v2H13z" fill="#f4c3c5"/></svg><p class="quote"><span>“At vero eos et accusamus et io dignissimos</span><span>ducimus qui bl vero eos et accusamus et</span><span>iustodio dignissimoss qui blanditiipraesnt</span><span>iuatum deleniti atq”</span></p><div class="sig">JOHN DOE <span class="stars">★★★★★</span></div></div>
  </div>
</section>

<!-- Screen 2: request type menu -->
<section class="screen" style="top:623px">
  <div class="btn btn-request" style="left:423px;top:13px">Request Feedback</div>
  <div class="btn btn-respond" style="left:701px;top:13px">Respond to Feedback</div>
  <div class="grid">
    <div class="card"><svg class="avatar" viewBox="0 0 53 53"><circle cx="26.5" cy="26.5" r="24.5" fill="none" stroke="#f4c3c5" stroke-width="3"/><circle cx="26.5" cy="21" r="7" fill="#f4c3c5"/><path d="M13 37c0-6 6-8 13.5-8s13.5 2 13.5 8v2H13z" fill="#f4c3c5"/></svg><p class="quote"><span>“At vero eos et accusamus et io dignissimos</span><span>ducimus qui bl vero eos et accusamus et</span><span>iustodio dignissimoss qui blanditiipraesnt</span><span>iuatum deleniti atq”</span></p><div class="sig">JOHN DOE <span class="stars">★★★★★</span></div></div>
    <div class="card"></div>
    <div class="card"><svg class="avatar" viewBox="0 0 53 53"><circle cx="26.5" cy="26.5" r="24.5" fill="none" stroke="#f4c3c5" stroke-width="3"/><circle cx="26.5" cy="21" r="7" fill="#f4c3c5"/><path d="M13 37c0-6 6-8 13.5-8s13.5 2 13.5 8v2H13z" fill="#f4c3c5"/></svg><p class="quote"><span>“At vero eos et accusamus et io dignissimos</span><span>ducimus qui bl vero eos et accusamus et</span><span>iustodio dignissimoss qui blanditiipraesnt</span><span>iuatum deleniti atq”</span></p><div class="sig">JOHN DOE <span class="stars">★★★★★</span></div></div>
    <div class="card"><svg class="avatar" viewBox="0 0 53 53"><circle cx="26.5" cy="26.5" r="24.5" fill="none" stroke="#f4c3c5" stroke-width="3"/><circle cx="26.5" cy="21" r="7" fill="#f4c3c5"/><path d="M13 37c0-6 6-8 13.5-8s13.5 2 13.5 8v2H13z" fill="#f4c3c5"/></svg><p class="quote"><span>“At vero eos et accusamus et io dignissimos</span><span>ducimus qui bl vero eos et accusamus et</span><span>iustodio dignissimoss qui blanditiipraesnt</span><span>iuatum deleniti atq”</span></p><div class="sig">JOHN DOE <span class="stars">★★★★★</span></div></div>
    <div class="card"><div class="sig">JOHN DOE <span class="stars">★★★★★</span></div></div>
    <div class="card"><svg class="avatar" viewBox="0 0 53 53"><circle cx="26.5" cy="26.5" r="24.5" fill="none" stroke="#f4c3c5" stroke-width="3"/><circle cx="26.5" cy="21" r="7" fill="#f4c3c5"/><path d="M13 37c0-6 6-8 13.5-8s13.5 2 13.5 8v2H13z" fill="#f4c3c5"/></svg><p class="quote"><span>“At vero eos et accusamus et io dignissimos</span><span>ducimus qui bl vero eos et accusamus et</span><span>iustodio dignissimoss qui blanditiipraesnt</span><span>iuatum deleniti atq”</span></p><div class="sig">JOHN DOE <span class="stars">★★★★★</span></div></div>
    <div class="card"><svg class="avatar" viewBox="0 0 53 53"><circle cx="26.5" cy="26.5" r="24.5" fill="none" stroke="#f4c3c5" stroke-width="3"/><circle cx="26.5" cy="21" r="7" fill="#f4c3c5"/><path d="M13 37c0-6 6-8 13.5-8s13.5 2 13.5 8v2H13z" fill="#f4c3c5"/></svg><p class="quote"><span>“At vero eos et accusamus et io dignissimos</span><span>ducimus qui bl vero eos et accusamus et</span><span>iustodio dignissimoss qui blanditiipraesnt</span><span>iuatum deleniti atq”</span></p><div class="sig">JOHN DOE <span class="stars">★★★★★</span></div></div>
    <div class="card"><svg class="avatar" viewBox="0 0 53 53"><circle cx="26.5" cy="26.5" r="24.5" fill="none" stroke="#f4c3c5" stroke-width="3"/><circle cx="26.5" cy="21" r="7" fill="#f4c3c5"/><path d="M13 37c0-6 6-8 13.5-8s13.5 2 13.5 8v2H13z" fill="#f4c3c5"/></svg><p class="quote"><span>“At vero eos et accusamus et io dignissimos</span><span>ducimus qui bl vero eos et accusamus et</span><span>iustodio dignissimoss qui blanditiipraesnt</span><span>iuatum deleniti atq”</span></p><div class="sig">JOHN DOE <span class="stars">★★★★★</span></div></div>
    <div class="card"><svg class="avatar" viewBox="0 0 53 53"><circle cx="26.5" cy="26.5" r="24.5" fill="none" stroke="#f4c3c5" stroke-width="3"/><circle cx="26.5" cy="21" r="7" fill="#f4c3c5"/><path d="M13 37c0-6 6-8 13.5-8s13.5 2 13.5 8v2H13z" fill="#f4c3c5"/></svg><p class="quote"><span>“At vero eos et accusamus et io dignissimos</span><span>ducimus qui bl vero eos et accusamus et</span><span>iustodio dignissimoss qui blanditiipraesnt</span><span>iuatum deleniti atq”</span></p><div class="sig">JOHN DOE <span class="stars">★★★★★</span></div></div>
  </div>
  <div class="veil"></div>
  <div class="modal">
    <div class="modal-head">REQUEST FEEDBACK</div>
    <div class="modal-close"><svg width="18" height="18" viewBox="0 0 18 18"><path d="M2 2l14 14M16 2L2 16" stroke="#000" stroke-width="2.6" stroke-linecap="round"/></svg></div>
    <ul class="modal-list">
      <li>Adhoc Feedback</li>
      <li>Mid Year Feedback</li>
      <li>360 Feedback</li>
    </ul>
  </div>
</section>

<!-- Screen 3: adhoc feedback -->
<section class="screen" style="top:1145px">
  <h2 class="page-title">ADHOC FEEDBACK</h2>
  <div class="search">Search for colleagues <svg width="13" height="13" viewBox="0 0 13 13"><circle cx="5.5" cy="5.5" r="4" fill="none" stroke="#777" stroke-width="1.8"/><path d="M8.5 8.5l3.5 3.5" stroke="#777" stroke-width="2"/></svg></div>
  <div class="btn btn-request" style="left:427px;top:58px">Request Feedback</div>
  <div class="btn btn-respond" style="left:705px;top:58px">Respond to Feedback</div>
  <div class="questions">
    <div class="question active">
      <div class="q-title">WHY VERO EOS ET ACCUSAMUS ET IO DIO DIGNISSIMGNISSIMOO DIGNISSIMS DUCIM ?<svg width="16" height="16" viewBox="0 0 16 16"><path d="M2 14l1-4 8-8 3 3-8 8z" fill="#fff"/></svg></div>
      <p class="q-body">Evero eos et accusamus et io dignissimos ducimus qui bl vero eos et accusamus et iustodio dignissimoss qui blanditiipraesnt iuatum delenitiEvero eos et accusamus et io dignissimos ducimus qui bl vero eos et accusamus et iustodio dignissimoss qui blanditiipraesnt iuatum deleniti atq atq</p>
      <div class="q-tag">REQUEST</div>
    </div>
    <div class="question">
      <div class="q-title">WHAT ET ACCUSAMUS ET IO DIO DIGNISSIMGNISSIMOO DIGNISSIMS DUCIM ?</div>
      <p class="q-body">Evero eos et accusamus et io dignissimos ducimus qui bl vero eos et accusamus et iustodio dignissimoss qui blanditiipraesnt iuatum delenitiEvero eos et accusamus et io dignissimos ducimus qui bl vero eos et accusamus et iustodio dignissimoss qui blanditiipraesnt iuatum deleniti atq atq</p>
      <div class="q-tag">REQUEST</div>
    </div>
    <div class="question">
      <div class="q-title">WHY ET ACCUSAMUS ET IO DIO DIGNISSIMGNISSIMOO DIGNISSIMS DUCIM ?</div>
      <p class="q-body">Evero eos et accusamus et io dignissimos ducimus qui bl vero eos et accusamus et iustodio dignissimoss qui blanditiipraesnt iuatum delenitiEvero eos et accusamus et io dignissimos ducimus qui bl vero eos et accusamus et iustodio dignissimoss qui blanditiipraesnt iuatum deleniti atq atq</p>
      <div class="q-tag">REQUEST</div>
    </div>
  </div>
</section>

<!-- Screen 4: mid year feedback -->
<section class="screen" style="top:1668px">
  <h2 class="page-title">MID YEAR FEEDBACK</h2>
  <div class="search">Search for colleagues <svg width="13" height="13" viewBox="0 0 13 13"><circle cx="5.5" cy="5.5" r="4" fill="none" stroke="#777" stroke-width="1.8"/><path d="M8.5 8.5l3.5 3.5" stroke="#777" stroke-width="2"/></svg></div>
  <div class="btn btn-request" style="left:427px;top:58px">Request Feedback</div>
  <div class="btn btn-respond" style="left:705px;top:58px">Respond to Feedback</div>
  <div class="questions">
    <div class="question active">
      <div class="q-title">WHY VERO EOS ET ACCUSAMUS ET IO DIO DIGNISSIMGNISSIMOO DIGNISSIMS DUCIM ?</div>
      <p class="q-body">Evero eos et accusamus et io dignissimos ducimus qui bl vero eos et accusamus et iustodio dignissimoss qui blanditiipraesnt iuatum delenitiEvero eos et accusamus et io dignissimos ducimus qui bl vero eos et accusamus et iustodio dignissimoss qui blanditiipraesnt iuatum deleniti atq atq</p>
      <div class="q-tag">REQUEST</div>
    </div>
    <div class="question">
      <div class="q-title">WHAT ET ACCUSAMUS ET IO DIO DIGNISSIMGNISSIMOO DIGNISSIMS DUCIM ?</div>
      <p class="q-body">Evero eos et accusamus et io dignissimos ducimus qui bl vero eos et accusamus et iustodio dignissimoss qui blanditiipraesnt iuatum delenitiEvero eos et accusamus et io dignissimos ducimus qui bl vero eos et accusamus et iustodio dignissimoss qui blanditiipraesnt iuatum deleniti atq atq</p>
      <div class="q-tag">REQUEST</div>
    </div>
    <div class="question">
      <div class="q-title">WHY ET ACCUSAMUS ET IO DIO DIGNISSIMGNISSIMOO DIGNISSIMS DUCIM ?</div>
      <p class="q-body">Evero eos et accusamus et io dignissimos ducimus qui bl vero eos et accusamus et iustodio dignissimoss qui blanditiipraesnt iuatum delenitiEvero eos et accusamus et io dignissimos ducimus qui bl vero eos et accusamus et iustodio dignissimoss qui blanditiipraesnt iuatum deleniti atq atq</p>
      <div class="q-tag">REQUEST</div>
    </div>
  </div>
</section>

</body>
</html>
```